Finance cashflow waterfall graphic

Recreate "Cashflow Waterfall Example 1" - waterfall term used to explain the different accounts and priority that need to be paid as part of a apartment building / project. Create simple, business professional graphic for real estate report. Check the inspiration image but change to dorm building, no people - potentially combine the two images... Ideally editable so I can change the names of the accounts / colors / etc.

```html
<!DOCTYPE html>
<html lang="en">
<head>
<meta charset="utf-8">
<title>Cashflow Waterfall</title>
<link href="https://fonts.googleapis.com/css2?family=Oswald:wght@500&family=Passion+One:wght@700&display=swap" rel="stylesheet">
<style>
  :root {
    --bg: #fdf0d8;
    --step: #4a2a3a;
    --band-fill: #f2d7b0;
    --accent: #e8892a;
    --label: #ffffff;
    --title-fill: #f4d4a8;
    --water: #1aa9c4;
    --water-light: #7fd0de;
  }
  html, body {
    margin: 0;
    padding: 0;
    width: 1134px;
    height: 1200px;
    overflow: hidden;
    background: var(--bg);
  }
  .waterfall { display: block; }
  .title {
    font-family: "Passion One", "Arial Narrow", sans-serif;
    font-weight: 700;
    font-size: 108px;
    fill: var(--title-fill);
    stroke: var(--accent);
    stroke-width: 2;
  }
  .step { fill: var(--step); }
  .step-label {
    font-family: "Oswald", "Arial Narrow", sans-serif;
    font-weight: 500;
    font-size: 24px;
    fill: var(--label);
  }
  .band { fill: var(--band-fill); stroke: var(--accent); stroke-width: 1.2; }
  .private-bar { fill: var(--accent); }
  .private-label { fill: var(--step); }
  .bucket { fill: url(#water-grad); }
</style>
</head>
<body>
<svg class="waterfall" width="1134" height="1200" viewBox="0 0 1134 1200" xmlns="http://www.w3.org/2000/svg">
  <defs>
    <linearGradient id="water-grad" x1="0" y1="0" x2="0" y2="1">
      <stop offset="0" stop-color="var(--water-light)"/>
      <stop offset="1" stop-color="var(--water)"/>
    </linearGradient>
  </defs>

  <text class="title" x="298" y="278" textLength="784" lengthAdjust="spacingAndGlyphs">Cashflow Waterfall</text>

  <g class="bands">
    <path class="band" d="M250 345 H1135 V392 H288 A38 38 0 0 1 250 354 Z"/>
    <path class="band" d="M345 466 H1135 V513 H383 A38 38 0 0 1 345 475 Z"/>
    <path class="band" d="M422 588 H1135 V635 H460 A38 38 0 0 1 422 597 Z"/>
    <path class="band" d="M506 709 H1135 V756 H544 A38 38 0 0 1 506 718 Z"/>
    <path class="band" d="M589 830 H1135 V877 H627 A38 38 0 0 1 589 839 Z"/>
    <path class="band" d="M721 951 H1135 V998 H759 A38 38 0 0 1 721 960 Z"/>
  </g>

  <g class="steps">
    <path class="step" d="M0 345 H151 V362 A30 30 0 0 1 121 392 H0 Z"/>
    <text class="step-label" x="64" y="378" textLength="68" lengthAdjust="spacingAndGlyphs">Revenue</text>

    <path class="step" d="M0 466 H232 V483 A30 30 0 0 1 202 513 H0 Z"/>
    <text class="step-label" x="68" y="499" textLength="149" lengthAdjust="spacingAndGlyphs">Operating Expense</text>

    <path class="step" d="M0 588 H315 V605 A30 30 0 0 1 285 635 H0 Z"/>
    <text class="step-label" x="151" y="621" textLength="146" lengthAdjust="spacingAndGlyphs">Debt Management</text>

    <path class="step" d="M0 709 H397 V726 A30 30 0 0 1 367 756 H0 Z"/>
    <text class="step-label" x="194" y="742" textLength="187" lengthAdjust="spacingAndGlyphs">Asset Management Fee</text>

    <path class="step" d="M0 830 H480 V847 A30 30 0 0 1 450 877 H0 Z"/>
    <text class="step-label" x="260" y="863" textLength="201" lengthAdjust="spacingAndGlyphs">Recapitalization Account</text>

    <path class="step" d="M0 951 H560 V968 A30 30 0 0 1 530 998 H0 Z"/>
    <text class="step-label" x="421" y="984" textLength="106" lengthAdjust="spacingAndGlyphs">Incentive Fee</text>

    <rect class="private-bar" x="660" y="1079" width="475" height="47"/>
    <path class="step" d="M0 1079 H704 V1096 A30 30 0 0 1 674 1126 H0 Z"/>
    <text class="step-label" x="257" y="1112" textLength="405" lengthAdjust="spacingAndGlyphs">Sustainable Reserve / Member Distribution (60%)</text>
    <text class="step-label private-label" x="706" y="1112" textLength="420" lengthAdjust="spacingAndGlyphs">Private Return / Managing Member Distribution (40%)</text>
  </g>

  <g role="img" aria-label="Bucket of water with tap dripping into the next step"><rect class="bucket" x="80" y="253" width="85" height="89"/></g>
  <g role="img" aria-label="Bucket of water with tap dripping into the next step"><rect class="bucket" x="163" y="374" width="85" height="89"/></g>
  <g role="img" aria-label="Bucket of water with tap dripping into the next step"><rect class="bucket" x="246" y="495" width="85" height="89"/></g>
  <g role="img" aria-label="Bucket of water with tap dripping into the next step"><rect class="bucket" x="329" y="616" width="84" height="89"/></g>
  <g role="img" aria-label="Bucket of water with tap dripping into the next step"><rect class="bucket" x="411" y="737" width="84" height="89"/></g>
  <g role="img" aria-label="Bucket of water with tap dripping into the next step"><rect class="bucket" x="493" y="858" width="85" height="89"/></g>
  <g role="img" aria-label="Bucket of water for member distribution"><rect class="bucket" x="537" y="988" width="84" height="89"/></g>
  <g role="img" aria-label="Bucket of water for managing member distribution"><rect class="bucket" x="633" y="988" width="85" height="89"/></g>
</svg>
</body>
</html>
```